EOFYS BANNER REQUIRED FOR HIGH-END BABY PRODUCT

We seel baby beanbags, and we need a banner for our annual END OF FINANCIAL YEAR SALE (EOFYS) about 700x900px.

The promo will be:

THE EOFYS SALE IS ON NOW!
30% OFF ALL ORDERS OVER $149 WITH CODE: EOFYS

We will use this banner for an email marketing campaign, and we will actually need to resize this banner to suit some affiliate marketing sizes too (ie: leaderboard etc), so if you are able to show your design in a few different sizes, that would be great.

We don't have alot of images for you to work off, so it will be your creative design skills that make it great.

Please keep in mind this is for a massive event that we will be competing with alot of other businesses for, as it is an annual event where the whole country goes on sale. We are in the process of building a photo studio so we have attached the images we have to work with now.

I have uploaded some of our patterns for you. This is CONFIDENTIAL. You are welcome to use these patterns in the dsign if you like.

Please, do your best.

Urban mums who crave design and function more than a cheap product.

Baby

• montserrat; intro rust; Pirou

b768aa
e667a6
f68e4e
fece3e
fbf289
add136
cadf82
33b8a4
33a6d7

• One, or both, of the two images upload. They are: IMG.5251 / IMG. 5253
• Would love a toddler in the pic also, if possible...they don't have to be using our beanbag, but there should be a pic of our beanbag there, as if it is waiting for them to use.
• Other brands. Childish themes. Too much vector overload...but some is awesome.

```html
<!DOCTYPE html>
<html lang="en">
<head>
<meta charset="utf-8">
<title>EOFYS Sale Leaderboard</title>
<link rel="stylesheet" href="https://fonts.googleapis.com/css2?family=Oswald:wght@200;300;500&family=Rubik+Dirt&display=swap">
<style>
  :root {
    --grey-text: #8f8f8f;
    --dark-text: #3a3a3a;
    --orange: #f68e4e;
    --pink: #e667a6;
    --mauve: #b768aa;
    --yellow: #fbf289;
    --lime: #cadf82;
    --teal: #33b8a4;
    --sky: #33a6d7;
    --brown: #9a7a62;
    --panel: #ffffff;
  }
  * { box-sizing: border-box; margin: 0; padding: 0; }
  html, body { width: 1200px; height: 148px; overflow: hidden; background: #fff; }
  .banner {
    position: relative;
    width: 1200px;
    height: 148px;
    overflow: hidden;
    font-family: "Oswald", sans-serif;
  }
  .banner__backdrop {
    position: absolute;
    inset: 0;
    background:
      linear-gradient(180deg, rgba(255,255,255,0.35) 0%, rgba(255,255,255,0) 50%, rgba(255,255,255,0.35) 100%),
      linear-gradient(90deg, #f3d9e6 0%, #f8efc4 18%, #e3eec6 36%, #d8ebef 54%, #f0dccb 72%, #e8dff0 88%, #f3d9e6 100%);
  }
  .banner__panel {
    position: absolute;
    left: 185px;
    top: 13px;
    width: 1005px;
    height: 119px;
    background: var(--panel);
  }
  .banner__photo-left {
    position: absolute;
    left: 0;
    top: 0;
    width: 185px;
    height: 148px;
    background:
      radial-gradient(ellipse 70% 45% at 40% 30%, #f4eee6 0%, rgba(244,238,230,0) 100%),
      linear-gradient(180deg, #e9e4d8 0%, #d8dcae 45%, #e7d3bd 70%, #c9a27e 100%);
  }
  .banner__headline {
    position: absolute;
    left: 218px;
    top: 20px;
    font-weight: 200;
    font-size: 37px;
    line-height: 56px;
    letter-spacing: 0.5px;
    color: var(--grey-text);
    text-transform: uppercase;
    white-space: nowrap;
  }
  .banner__headline .accent { color: var(--orange); font-weight: 300; }
  .banner__discount {
    position: absolute;
    left: 478px;
    top: 54px;
    font-family: "Rubik Dirt", sans-serif;
    font-size: 31px;
    line-height: 40px;
    color: var(--dark-text);
    letter-spacing: 1px;
    white-space: nowrap;
  }
  .banner__photo-frame {
    position: absolute;
    left: 664px;
    top: -4px;
    width: 292px;
    height: 156px;
    padding: 7px;
    background: #fff;
    transform: rotate(-1.5deg);
    box-shadow: 0 2px 6px rgba(0,0,0,0.2);
  }
  .banner__photo-right {
    width: 100%;
    height: 100%;
    background:
      radial-gradient(ellipse 40% 50% at 30% 65%, #e7c9b4 0%, rgba(231,201,180,0) 100%),
      radial-gradient(ellipse 30% 60% at 80% 55%, #ece6e0 0%, rgba(236,230,224,0) 100%),
      linear-gradient(120deg, #f1ebe4 0%, #d8cfc6 50%, #e6d2d8 100%);
  }
  .banner__terms {
    position: absolute;
    left: 985px;
    top: 48px;
    font-size: 20px;
    line-height: 25px;
    font-weight: 300;
    color: var(--dark-text);
    text-transform: uppercase;
    letter-spacing: 0.3px;
    white-space: nowrap;
  }
  .banner__terms strong { font-weight: 500; }
</style>
</head>
<body>
  <div class="banner">
    <div class="banner__backdrop" role="img" aria-label="Pastel polka-dot pattern in pink, yellow, lime, blue and brown"></div>
    <div class="banner__panel"></div>
    <div class="banner__photo-left" role="img" aria-label="Photo of a baby lying in a patterned baby beanbag"></div>
    <h1 class="banner__headline">The <span class="accent">Eofys</span> Sale<br>Is <span class="accent">On Now!</span></h1>
    <p class="banner__discount">30% OFF</p>
    <div class="banner__photo-frame">
      <div class="banner__photo-right" role="img" aria-label="Photo of a toddler beside a baby in a polka-dot beanbag"></div>
    </div>
    <p class="banner__terms">All orders over <strong>$149</strong><br>with code: <strong>EOFYS</strong></p>
  </div>
</body>
</html>
```